Affiliate website design and wireframe

We need a design of an affiliate website for an application we purchased, it is important that you build the website pages according to the developer of the applications specifications (please see attached documents) the developer of the application will configure the pages and add them to the site. Please take special note of his comments below.

We all so need you to create a wire frame so the developer can test everything (http://quartz.lomeriva.vn/)

It will be the homepage and about 16 inner pages (please see attached files)
Here is our website http://maplecourtlink.com/affiliate/affiliates/index.php

The version of the software we purchased is the Quill Partner Grid version

Comments from the developers

1. I will need the source files of the design (photoshop .psd files and font files if custom fonts are used), since the implementation is closely bound to component sizes (like border width, margin width etc.) and colors. If you own a corporate design manual, it's crucial to send it as well. Also, please, make sure if you use custom fonts, that these allow legal website integration (like zorvix web fonts).

2. Any and every content is controlled via templates. All editing/adding/removing etc. is done here. The template files are essentially html/php documents, they use a template engine called brisko (http://www.brisko.net/) which has it's own language similar to php.

3. .psd files are ideal, because we deal with the specifics of QPS/QPG implementation on a daily basis. Any html/css developed in advance may prove to be a poor choice. You may choose to let an in-house developer do the job, but experience wise this is more costly, since he will not be accustomed to the template/functionality systems of QPS/QPG.

4. I will need the source files of the design (photoshop .psd files and font files if custom fonts are used), since the implementation is closely bound to component sizes (like border width, margin width etc.) and colors. If you own a corporate design manual, it's crucial to send it as well. Also, please, make sure if you use custom fonts, that these allow legal website integration (like zorvix web fonts).

Regards,

Tomas Vereck

We prefer illustrations more than pictures of real people.

This is the home page, it is asking for Merchant and Affiliate sign up, not just affiliate.

http://maplecourtlink.com/affiliate/index.php

Please note the home page features both Merchant and Affiliate sign up

We are looking for illustration design not just stock images

Please remember the search menu that searches for the available programs, see the example we gave you, look at the search menu at the top of the page http://www.tradolink.com/

We are reviewing everything, no need to send more designs

Target Market(s)

Natural Products Manufacturers
Natural products Sales reps
Natural Products Bloggers
Social Marketing

Industry/Entity Type

Software

Requirements
Must have
• 1. All links on pages should go to the appropriate pages.
2. Colors can be based on our logo design (look at the attachments)
3. Here is our website http://maplecourtlink.com/affiliate/affiliates/index.php
4. We have attached a drawing of how we think the homepage concept should follow.
5. Main concept of design, is trying to show our sales people (Affiliates) are doing multiple things to advertise and sell the merchants products.(see logo)
6. Need to be able to edit all text and images.
7. Our target audience is Natural product sales people (Advertisers, bloggers, ext) and natural product manufacturers.
8. You can speak to the company who made the application, through live chat, on there website http://www.quillpartnergrid.com/
Nice to have
• See Attached Documents.
site should take up whole website pages
Look For fun Illustrated Website, one of the better ones we have seen is http://www.tradolink.com/index.cfm
Should not have
• Please look very carefully at developers comment above.

```html
<!DOCTYPE html>
<html lang="en">
<head>
<meta charset="utf-8">
<title>Maplecourt Link – Affiliate Network</title>
<link rel="stylesheet" href="https://fonts.googleapis.com/css2?family=Open+Sans:wght@300;400;600;700&display=swap">
<style>
:root{
  --page-bg:#e4e4e4;
  --nav-bg:#6b6b6b;
  --nav-active:#5a5a5a;
  --hero-band:#c4524c;
  --call-band:#dcdcdc;
  --content-bg:#f4f4f4;
  --panel:#f7f7f7;
  --footer:#3b3b3d;
  --footer-line:#4c4c4e;
  --red:#e2433d;
  --yellow:#f4b60a;
  --text:#555;
  --muted:#8d8d8d;
  --white:#fff;
  --feature-box:#e6e6e6;
}
*{box-sizing:border-box;margin:0;padding:0}
html,body{width:1200px;height:936px;overflow:hidden}
body{position:relative;background:var(--page-bg);font-family:Arial,Helvetica,sans-serif;color:var(--text)}
.abs{position:absolute}

.band-nav{left:0;top:78px;width:1200px;height:41px;background:var(--nav-bg)}
.band-hero{left:0;top:119px;width:1200px;height:267px;background:var(--hero-band);
  background-image:repeating-linear-gradient(0deg,rgba(0,0,0,.06) 0 1px,transparent 1px 3px),repeating-linear-gradient(90deg,rgba(0,0,0,.06) 0 1px,transparent 1px 3px)}
.band-call{left:0;top:386px;width:1200px;height:79px;background:var(--call-band)}
.band-content{left:0;top:465px;width:1200px;height:306px;background:var(--content-bg)}
.band-footer{left:0;top:771px;width:1200px;height:165px;background:var(--footer)}

.header{left:229px;top:0;width:742px;height:78px;overflow:hidden;background:#f6f6f6}
.brand{left:59px;top:28px;display:flex;align-items:center;gap:8px;font-family:"Open Sans",Arial,sans-serif;font-weight:700;font-size:17px;color:#2f7d32;letter-spacing:.3px}
.brand-mark{width:14px;height:14px;border-radius:50%;background:#2f7d32}
.btn{display:inline-block;border-radius:3px;font-family:"Open Sans",Arial,sans-serif;font-size:14px;font-weight:400;text-align:center;white-space:nowrap;box-shadow:0 1px 2px rgba(0,0,0,.4)}
.btn-red{background:var(--red);color:var(--white)}
.btn-yellow{background:var(--yellow);color:#3a3a3a}
.btn-login{top:31px;height:29px;line-height:29px;letter-spacing:-.3px}

.nav{left:229px;top:78px;width:742px;height:41px}
.nav a{position:absolute;top:0;color:#f2f2f2;text-decoration:none;font-family:"Open Sans",Arial,sans-serif;font-size:14px;letter-spacing:-.3px;height:41px;line-height:41px;white-space:nowrap}
.nav a.active{background:var(--nav-active);width:72px;left:0;padding-left:20px}
.follow{left:781px;top:78px;height:41px;display:flex;align-items:center;gap:9px;color:#fff;font-family:"Open Sans",Arial,sans-serif;font-weight:600;font-size:13px}
.follow .dot{width:7px;height:7px;border-radius:50%;background:#fff}

.hero{left:229px;top:119px;width:742px;height:267px;overflow:hidden}
.hero-copy{left:16px;top:66px;width:275px}
.hero-kicker{font-family:"Open Sans",Arial,sans-serif;font-weight:600;font-size:25px;color:var(--yellow);letter-spacing:-.8px;line-height:30px}
.hero-title{font-family:"Open Sans",Arial,sans-serif;font-weight:300;font-size:32px;color:var(--red);letter-spacing:-1px;line-height:36px}
.hero-text{margin-top:4px;width:262px;font-size:10px;font-weight:700;color:#fff;line-height:12.5px;letter-spacing:-.1px}
.hero-btn{left:17px;top:193px;width:97px;height:28px;line-height:28px;font-weight:300}

.call-phone{left:256px;top:418px}
.call-label{left:284px;top:418px;font-family:"Open Sans",Arial,sans-serif;font-size:14px;font-weight:300;letter-spacing:-.3px;color:#555;white-space:nowrap}
.call-divider{left:470px;top:403px;width:1px;height:45px;background:#bcbcbc}
.call-text{left:511px;top:408px;width:282px;font-size:10.5px;line-height:13px;color:#555}
.call-btn{left:811px;top:412px;width:98px;height:29px;line-height:29px;font-weight:300}

.content{left:229px;top:465px;width:742px;height:330px;background:var(--panel)}
.col{position:absolute;top:0;height:310px}
.col-about{left:0;width:246px}
.col-how{left:246px;width:258px;background:#f8f8f8;box-shadow:0 0 10px rgba(0,0,0,.08)}
.col-feature{left:504px;width:238px}
.col-head{position:absolute;top:32px;display:flex;align-items:center;gap:9px;font-family:"Open Sans",Arial,sans-serif;font-size:13px;font-weight:600;color:#444;white-space:nowrap}
.col-head.red{color:var(--red);font-weight:400}
.about-text{position:absolute;left:25px;top:77px;width:200px;font-size:10.5px;line-height:12.5px;color:#8f8f8f}
.steps{position:absolute;left:17px;top:67px;width:218px;list-style:none;font-size:10.5px;line-height:15px;color:#444}
.steps li{position:relative;padding-left:18px}
.steps li::before{content:"";position:absolute;left:0;top:5px;width:6px;height:3px;background:var(--red)}
.steps li::after{content:"";position:absolute;left:5px;top:3px;border-left:4px solid var(--red);border-top:3.5px solid transparent;border-bottom:3.5px solid transparent}
.feature-box{position:absolute;left:17px;width:202px;background:var(--feature-box);font-family:"Open Sans",Arial,sans-serif;font-size:12.5px;letter-spacing:-.5px;color:#555;line-height:16px;padding:1px 4px}
.feature-note{position:absolute;left:17px;top:210px;width:205px;font-size:10.5px;line-height:12.5px;color:#333}

.footer-title{left:233px;top:827px;font-family:"Open Sans",Arial,sans-serif;font-weight:600;font-size:14px;color:#fff}
.footer-info{top:855px;font-size:10px;color:var(--muted);white-space:nowrap;display:flex;align-items:center;gap:4px}
.footer-info i{display:inline-block;width:7px;height:7px;border-radius:50%;background:var(--muted)}
.footer-rule{left:232px;top:877px;width:563px;height:1px;background:var(--footer-line)}
.footer-links{left:232px;top:887px;display:flex;gap:15px;font-size:10.5px;color:var(--muted);white-space:nowrap}
.footer-social{left:858px;top:808px;list-style:none;font-size:10.5px;line-height:18.8px;color:var(--muted)}
.footer-social li{display:flex;align-items:center;gap:8px}
.footer-social i{width:6px;height:6px;border-radius:50%;background:var(--muted);display:inline-block}
.bottom-rule{left:0;top:909px;width:1200px;height:1px;background:#2e2e30}
.copyright{left:233px;top:917px;font-size:10.5px;color:var(--muted)}
</style>
</head>
<body>
<div class="abs band-nav"></div>
<div class="abs band-hero"></div>
<div class="abs band-call"></div>
<div class="abs band-content"></div>
<div class="abs band-footer"></div>

<header class="abs header">
  <svg class="abs" style="left:0;top:0" width="742" height="78" viewBox="0 0 742 78">
    <path d="M330 78 Q370 10 470 0 L742 0 L742 78 Z" fill="#3b3b3b"/>
    <path d="M330 78 Q370 10 470 0 L455 0 Q355 12 320 78 Z" fill="#e2433d"/>
  </svg>
  <div class="abs brand"><span class="brand-mark"></span>Maplecourt Link</div>
  <a class="abs btn btn-red btn-login" style="left:485px;width:98px">Affiliate Login</a>
  <a class="abs btn btn-yellow btn-login" style="left:591px;width:112px">Merchant Login</a>
</header>

<nav class="abs nav">
  <a class="active">Home</a>
  <a style="left:80px">About Us</a>
  <a style="left:157px">Services</a>
  <a style="left:228px">Partners</a>
  <a style="left:301px">Sign Up</a>
  <a style="left:370px">Contact Us</a>
</nav>
<div class="abs follow">Follow Us:<span class="dot"></span><span class="dot"></span><span class="dot"></span><span class="dot"></span><span class="dot"></span></div>

<section class="abs hero">
  <svg class="abs" style="left:0;top:0" width="742" height="267" viewBox="0 0 742 267">
    <defs>
      <linearGradient id="heroDark" x1="0" y1="0" x2="1" y2="1">
        <stop offset="0" stop-color="#454545"/><stop offset="1" stop-color="#2f2f2f"/>
      </linearGradient>
      <linearGradient id="heroPhoto" x1="0" y1="0" x2="1" y2="1">
        <stop offset="0" stop-color="#9aa2a8"/><stop offset=".5" stop-color="#5e6570"/><stop offset="1" stop-color="#2e3440"/>
      </linearGradient>
    </defs>
    <rect width="742" height="267" fill="url(#heroDark)"/>
    <path d="M310 0 Q260 150 400 267 L742 267 L742 0 Z" fill="url(#heroPhoto)" role="img" aria-label="Photo of a cheering businessman in a suit in front of city office towers"/>
    <path d="M310 0 Q260 150 400 267 L392 267 Q250 150 296 0 Z" fill="#e2433d"/>
  </svg>
  <div class="abs hero-copy">
    <div class="hero-kicker">Become a Member</div>
    <div class="hero-title">Proin gravida nibh</div>
    <p class="hero-text">Lorem Ipsum. Proin gravida nibh vel velit auctor aliquet. Aenean sollicitudin, lorem quis bibendum auctor, nisi elit consequat ipsum, nec sagittis sem nibh id elit.</p>
  </div>
  <a class="abs btn btn-red hero-btn">Read more..</a>
</section>

<svg class="abs call-phone" width="18" height="20" viewBox="0 0 18 20"><path d="M3 1 L7 1 L8 6 L5.5 7.5 Q7 12 11 14.5 L12.5 12 L17 13 L17 17 Q16 19 13 19 Q3 16 1 5 Q1 2 3 1 Z" fill="#777"/></svg>
<div class="abs call-label">Call Now: +123 456 7890</div>
<div class="abs call-divider"></div>
<p class="abs call-text">Signing up and getting your account configured couldn't be easier. You can be referring business our way in as little as five minutes.</p>
<a class="abs btn btn-red call-btn">Join Now!</a>

<main class="abs content">
  <section class="col col-about">
    <h2 class="col-head" style="left:26px"><svg width="17" height="22" viewBox="0 0 17 22"><circle cx="8.5" cy="5" r="4.5" fill="#555"/><path d="M0 22 Q0 11 8.5 11 Q17 11 17 22 Z" fill="#333"/><path d="M7.5 11 L9.5 11 L9 18 L8 18 Z" fill="#e2433d"/></svg>Who we are?</h2>
    <p class="about-text">Lorem ipsum dolor sit amet, consectetur adipisicing elit, sed do eiusmod tempor incididunt ut labore et dolore magna aliqua. Ut enim ad minim veniam, quis nostrud exercitation ullamco laboris nisi ut aliquip ex ea commodo consequat. Duis aute irure dolor in reprehenderit in voluptate velit esse cillum dolore eu fugiat nulla pariatur. Excepteur sint occaecat</p>
  </section>
  <section class="col col-how">
    <h2 class="col-head red" style="left:20px"><svg width="20" height="20" viewBox="0 0 20 20"><circle cx="10" cy="10" r="10" fill="#2a63b8"/><text x="10" y="15" text-anchor="middle" font-family="Arial" font-weight="700" font-size="14" fill="#fff">?</text></svg>How Does it work?</h2>
    <ul class="steps">
      <li>Visitor clicks on an affiliate link on your site or in an email.</li>
      <li>The visitors IP is logged and a cookie is placed in their browser for tracking purposes.</li>
      <li>The visitor browses our site, and may decide to order.</li>
      <li>If the visitor orders (the order need not be placed during the same browser session--cookies and IPs are stored indefinitely), the order will be registered as a sale for you.</li>
      <li>We will review and approve the sale.<br>You will receive commission payouts.</li>
    </ul>
  </section>
  <section class="col col-feature">
    <h2 class="col-head" style="left:16px"><svg width="19" height="18" viewBox="0 0 19 18"><path d="M1 9 L4 7 L7 12 L16 0 L19 1 L7 18 Z" fill="#234c8a"/></svg>Feature</h2>
    <div class="feature-box" style="top:71px;height:33px">Earn up to 50% commission for all products!</div>
    <div class="feature-box" style="top:121px;height:33px">High Conversion Rate = More Money.</div>
    <div class="feature-box" style="top:171px;height:33px;line-height:28px">Long cookie duration.</div>
    <p class="feature-note">If a customer comes from your site to ours, and then comes back to purchase six months later, you get credit.</p>
  </section>
</main>

<h3 class="abs footer-title">Contact Information</h3>
<div class="abs footer-info" style="left:232px"><i></i>Proin gravida nibh vel velit auctor aliquet, UK.</div>
<div class="abs footer-info" style="left:459px"><i></i>Email: info@brightmeadowapps.com</div>
<div class="abs footer-info" style="left:633px"><i></i>Email: info@brightmeadowapps.com</div>
<div class="abs footer-rule"></div>
<div class="abs footer-links"><span>Privacy</span><span>|</span><span>Policy</span><span>|</span><span>Legal Notice</span><span>|</span><span>Terms of Service</span><span>|</span><span>FAQs</span></div>
<ul class="abs footer-social">
  <li><i></i>Facelane</li><li><i></i>Chirpline</li><li><i></i>Linkwork</li><li><i></i>Circleplus</li><li><i></i>RSS Feeds</li>
</ul>
<div class="abs bottom-rule"></div>
<div class="abs copyright">© Copyright MAPLECOURTLINK 2013</div>
</body>
</html>
```